Velmora Investment Management Needs Door Wording Design

We need someone to put together a design for our glass front doors (2).

The words could be, but aren't limited to, as follows:

"100
Serenely Restorative Bodywork
*Ring Bell"

and

"200 & 300
Velmora Investment Management inc.
*Ring Bell"

The design should be clean, subtle and professional. It is a simple mainly glass door with a black frame. Our website is www.velmorainvest.ca for a more detailed description of what we do. The adjacent business would also be involved, as per the wording of the Serenely Restorative Bodywork.

We are looking for something to bring out the wording on the door (there is currently a piece of paper printed and taped to the inside).

Dimensions of the window are 47 inches x 23 inches.

Thanks!

Colors
000000
ffffff

Requirements
Must have
• The previous words
Nice to have
• Creative flair, taking into consideration the nature of our business (Investment Management)

```html
<!DOCTYPE html>
<html lang="en">
<head>
<meta charset="utf-8">
<title>Velmora Project – Door Wording</title>
<link rel="stylesheet" href="https://fonts.googleapis.com/css2?family=Bebas+Neue&family=Open+Sans:wght@400&display=swap">
<style>
  :root {
    --ink: #000000;
    --paper: #ffffff;
  }
  html, body {
    margin: 0;
    padding: 0;
    width: 927px;
    height: 1200px;
    overflow: hidden;
    background: var(--paper);
  }
  .sheet {
    position: relative;
    width: 927px;
    height: 1200px;
    background: var(--paper);
    color: var(--ink);
  }
  .title-block {
    position: absolute;
    left: 126px;
    top: 24px;
    width: 771px;
    height: 75px;
    border: 1.5px solid var(--ink);
    box-sizing: border-box;
    font-family: "Open Sans", sans-serif;
    font-size: 22px;
    line-height: 36px;
    text-align: right;
    padding: 4px 10px 0 0;
  }
  .door-panel {
    position: absolute;
    border: 1.5px solid var(--ink);
    box-sizing: border-box;
  }
  .door-panel--massage { left: 62px; top: 246px; width: 339px; height: 691px; }
  .door-panel--invest  { left: 526px; top: 244px; width: 340px; height: 691px; }
  .suite-frames {
    position: absolute;
    left: 0;
    top: 0;
  }
  .word {
    position: absolute;
    margin: 0;
    font-family: "Bebas Neue", sans-serif;
    font-weight: 400;
    line-height: 1;
    white-space: nowrap;
    color: var(--ink);
  }
  .suite-number { font-size: 71px; letter-spacing: 5px; top: 341px; }
</style>
</head>
<body>
<main class="sheet">
  <header class="title-block">VELMORA PROJECT<br>MARCH 13, 2017</header>

  <div class="door-panel door-panel--massage"></div>
  <div class="door-panel door-panel--invest"></div>

  <svg class="suite-frames" width="927" height="1200" viewBox="0 0 927 1200" aria-hidden="true">
    <g fill="none" stroke="var(--ink)" stroke-width="6.5" stroke-linejoin="miter">
      <path d="M100 398 H90 V271 H221 V332"/>
      <path d="M561 398 H551 V271 H681 V332"/>
      <path d="M718 398 H708 V271 H838 V332"/>
    </g>
  </svg>

  <span class="word suite-number" style="left:116px;">100</span>
  <h2 class="word" style="left:85px; top:483px; font-size:46px; letter-spacing:1px;">SERENELY</h2>
  <h2 class="word" style="left:85px; top:530px; font-size:64px;">RESTORATIVE</h2>
  <h2 class="word" style="left:85px; top:607px; font-size:86px; letter-spacing:1px;">BODYWORK</h2>
  <p class="word" style="left:86px; top:774px; font-size:57px;">RELAX</p>
  <p class="word" style="left:86px; top:825px; font-size:69px;">NOW</p>
  <p class="word" style="left:86px; top:892px; font-size:16px; letter-spacing:0.5px;">JUST RING THE BELL</p>

  <span class="word suite-number" style="left:576px;">200</span>
  <span class="word suite-number" style="left:734px;">300</span>
  <h1 class="word" style="left:549px; top:490px; font-size:96px; letter-spacing:2px;">VELMORA</h1>
  <h2 class="word" style="left:549px; top:606px; font-size:63px;">INVESTMENT</h2>
  <h2 class="word" style="left:549px; top:668px; font-size:43px;">MANAGEMENT INC.</h2>
  <p class="word" style="left:549px; top:774px; font-size:57px;">INVEST</p>
  <p class="word" style="left:549px; top:825px; font-size:69px;">NOW</p>
  <p class="word" style="left:550px; top:892px; font-size:16px; letter-spacing:0.5px;">JUST RING THE BELL</p>
</main>
</body>
</html>
```